Tri-Fold Brochure Redesign for Floral Preservation Business

I would like to redesign my current tri-fold brouchue that I created myself and have it updated. I would like to keep the same content, color and images, but have it redesigned to look fresher and updated. I'm in the the floral preservation business and work with brides in the wedding inductry. I'm looking for a royal/rustic feel and it should relate to the look and feel of my website www.larkmeadow.com. I have included the Photoshop file I used to create my orginal bouchure.

The only content that has changed is my address which is now;
2847 Birchfall Court, Reston VA 20173

Safe Zone Width - 10.875
Safe Zone Height - 8.375

I have included the Photoshop and Illustrator templates for the tri-fold brochure from the printer I will be using.

```html
<!DOCTYPE html>
<html lang="en">
<head>
<meta charset="utf-8">
<title>Lark Meadow Tri-Fold Brochure</title>
<link rel="stylesheet" href="https://fonts.googleapis.com/css2?family=Cinzel:wght@400;700&family=Arimo:wght@400;700&family=Pinyon+Script&display=swap">
<style>
  :root {
    --stage: #e4e1dc;
    --paper: #f4f4f4;
    --cream-1: #efe2cc;
    --cream-2: #dcc7a6;
    --crimson: #b3272d;
    --crimson-dark: #7e1a1e;
    --ink: #3a3a3a;
    --ink-soft: #5b5b5b;
    --link-blue: #2a4f8f;
    --frame-wood: #5b2a1a;
    --bead-blue: #5db3d8;
  }
  * { box-sizing: border-box; margin: 0; padding: 0; }
  html, body { width: 1200px; height: 900px; overflow: hidden; }
  body {
    background: var(--stage);
    font-family: "Arimo", Arial, sans-serif;
    color: var(--ink);
    position: relative;
  }
  .sheet {
    position: absolute;
    top: 228px;
    width: 575px;
    height: 444px;
    box-shadow: 0 4px 14px rgba(0,0,0,.18);
  }
  .sheet--outside { left: 17px; background: var(--paper); border: 1px solid #9a9a9a; }
  .sheet--inside { left: 608px; background: linear-gradient(160deg, var(--cream-1), var(--cream-2)); }

  .panel { position: absolute; top: 0; height: 100%; width: 191px; }
  .panel--1 { left: 0; } .panel--2 { left: 192px; } .panel--3 { left: 384px; }

  .brand { display: flex; flex-direction: column; align-items: center; }
  .brand__mark { width: 22px; height: 22px; background: var(--crimson); }
  .brand__name {
    font-family: "Cinzel", serif; font-weight: 400; color: var(--ink-soft);
    font-size: 15px; margin-top: 3px; letter-spacing: .5px;
  }
  .brand--large .brand__mark { width: 38px; height: 38px; }
  .brand--large .brand__name { font-size: 22px; }

  .heading {
    font-family: "Cinzel", serif; color: var(--crimson); font-weight: 700;
    text-align: center; letter-spacing: .5px;
  }
  .rule { width: 60px; height: 1px; background: var(--crimson); margin: 3px auto 0; }

  .about { position: absolute; top: 18px; left: 16px; right: 14px; }
  .about .heading { font-size: 11px; margin-top: 8px; }
  .about__body { font-size: 7.4px; line-height: 10.4px; margin-top: 9px; }
  .about__body p + p { margin-top: 9px; }
  .signature { font-family: "Pinyon Script", cursive; font-size: 16px; margin-top: 6px; }
  .about__role { font-size: 7.4px; line-height: 10.4px; margin-top: 8px; color: var(--ink-soft); }

  .social { position: absolute; top: 75px; left: 0; right: 0; text-align: center; }
  .social__row { display: flex; justify-content: center; align-items: center; gap: 6px; }
  .social__square { width: 16px; height: 16px; background: var(--link-blue); }
  .social__text { font-size: 7.4px; line-height: 9.5px; font-weight: 700; color: var(--link-blue); text-align: left; }
  .social__url { font-size: 7.4px; font-weight: 700; color: var(--link-blue); margin-top: 7px; }

  .contact { position: absolute; left: 0; right: 0; bottom: 38px; text-align: center; }
  .contact__note { font-size: 7.4px; color: var(--crimson); letter-spacing: .3px; margin-top: 14px; }
  .contact__lines { font-size: 7.4px; line-height: 10.5px; margin-top: 10px; color: var(--ink-soft); }

  .cover { position: absolute; top: 70px; left: 0; right: 0; }
  .cover__tagline {
    font-family: "Cinzel", serif; font-size: 7.6px; line-height: 10.5px; text-align: center;
    color: var(--ink); margin-top: 12px; letter-spacing: .3px;
  }

  .banner {
    position: absolute; top: 16px; left: 20px; width: 352px; height: 36px;
    background: var(--crimson-dark); color: #f4e6cf;
    font-family: "Cinzel", serif; font-size: 6.6px; line-height: 9px;
    text-align: center; padding: 5px 10px; letter-spacing: .2px;
  }
  .photo { position: absolute; top: 62px; width: 150px; height: 172px; }
  .photo--shadowbox {
    left: 36px; border: 9px solid var(--frame-wood);
    background: radial-gradient(circle at 50% 45%, #f3ead6 0 30%, #e5d5b8 55%, #cdb994 100%);
  }
  .photo--jewelry {
    left: 206px; border: 1px solid #b9b9b9;
    background: radial-gradient(ellipse at 50% 50%, var(--bead-blue) 0 14%, #9fcfe4 24%, #ffffff 42%);
  }
  .feature { position: absolute; top: 246px; width: 170px; text-align: center; }
  .feature--left { left: 26px; } .feature--right { left: 196px; }
  .feature .heading { font-size: 9.5px; font-weight: 400; }
  .feature__body { font-size: 6.6px; line-height: 9.3px; margin-top: 12px; text-align: left; }

  .process { position: absolute; top: 16px; left: 392px; width: 172px; }
  .process > .heading { font-size: 11px; font-weight: 400; }
  .step { margin-top: 8px; }
  .step__num { font-family: "Pinyon Script", cursive; color: var(--crimson); font-size: 17px; text-align: center; line-height: 18px; }
  .step .heading { font-size: 7.4px; font-weight: 400; margin-top: 4px; }
  .step__body { font-size: 6.6px; line-height: 9.3px; margin-top: 5px; }
  .process__note { font-size: 5.6px; line-height: 7.5px; color: var(--ink-soft); text-align: center; margin-top: 8px; }
</style>
</head>
<body>

<section class="sheet sheet--outside" aria-label="Brochure outside">
  <div class="panel panel--1">
    <div class="about">
      <div class="brand"><span class="brand__mark"></span><span class="brand__name">Lark Meadow</span></div>
      <h2 class="heading">About Us</h2>
      <div class="rule"></div>
      <div class="about__body">
        <p>With a rich family history in the floral business spanning over 60 years, I have spent the past two decades learning all aspects of the business but focusing primarily on perfecting the freeze-dry floral preservation process. Most recently I have expanded beyond the conventional freeze-dry offerings and have learned the art of creating flower petal jewelry from preserved flowers. I'm proud to be one of the few companies in the U.S. to offer this unique service.</p>
        <p>At Lark Meadow, we are committed to being the premiere floral preservation company in your community. I am extremely proud and honored to carry on the family name in the floral business by providing these services not only in my hometown of Washington DC but also in the Hampton Roads metro area. I'm confident the services offered by Lark Meadow are sure to exceed your expectations for years to come.</p>
      </div>
      <div class="signature">Owen Hartwell</div>
      <div class="about__role">Owner &amp; Operator<br>Lark Meadow</div>
    </div>
  </div>

  <div class="panel panel--2">
    <div class="social">
      <div class="social__row">
        <span class="social__square"></span>
        <span class="social__text">Become a fan and view<br>our most recent work</span>
      </div>
      <div class="social__url">www.friendpage.com/larkmeadow</div>
    </div>
    <div class="contact">
      <div class="brand"><span class="brand__mark"></span><span class="brand__name">Lark Meadow</span></div>
      <div class="contact__note">BY APPOINTMENT ONLY</div>
      <div class="contact__lines">2847 Birchfall Court, Reston VA 20173<br>703.555.0148 | www.larkmeadow.com</div>
    </div>
  </div>

  <div class="panel panel--3">
    <div class="cover">
      <div class="brand brand--large"><span class="brand__mark"></span><span class="brand__name">Lark Meadow</span></div>
      <p class="cover__tagline">The National Capital's Premier<br>Flower Preservation Professionals</p>
    </div>
    <div class="contact">
      <div class="contact__note">BY APPOINTMENT ONLY</div>
      <div class="contact__lines">2847 Birchfall Court, Reston VA 20173<br>703.555.0148 | www.larkmeadow.com</div>
    </div>
  </div>
</section>

<section class="sheet sheet--inside" aria-label="Brochure inside">
  <div class="banner">You Have Chosen The Perfect Flowers, Now Cherish The Perfect Way To Cherish Them. Lark Meadow's Floral Preservation Process Transforms Your Flowers Into Lasting Works of Art or Jewelry</div>

  <div class="photo photo--shadowbox" role="img" aria-label="Photo of a preserved bridal bouquet in a framed shadowbox"></div>
  <div class="photo photo--jewelry" role="img" aria-label="Photo of a bracelet with blue flower-petal beads and silver findings"></div>

  <div class="feature feature--left">
    <h3 class="heading">Floral Preservation</h3>
    <div class="rule"></div>
    <p class="feature__body">Our handcrafted shadowboxes are made with the industry's finest raw materials to ensure the highest level of quality. We use only select solid wood moulding from a family maker with over 100 years of craft. Every shadowbox is matted and mounted with archival materials that museums trust to protect the nation's most valuable artwork. We finish each piece with museum-grade glass to enhance, protect and beautify, adding to a museum-quality work of art.</p>
  </div>

  <div class="feature feature--right">
    <h3 class="heading">Flower-Petal Jewelry</h3>
    <div class="rule"></div>
    <p class="feature__body">If you would like to turn your memories into a wearable story, consider creating signature jewelry. We turn real petals from your blooms into one-of-a-kind jewelry pieces for you or your loved ones. We can transform your flowers into earrings, necklaces, bracelets, charm beads or rosaries. The tradition hails from the historical practice of nuns creating rosaries from condensed flower petals. In that same vein, we create unique pieces to fit your own style. Each piece is made by hand from your flowers and the highest quality sterling silver findings.</p>
  </div>

  <div class="process">
    <h2 class="heading">The Process</h2>
    <div class="rule"></div>
    <div class="step">
      <div class="step__num">Step 1</div>
      <h4 class="heading">Reserve The Date</h4>
      <p class="step__body">To ensure our services, you will need to "reserve the date" with a deposit. We accept no more than 4 clients a week and with over 50,000 weddings in the DC and Hampton Roads Metro areas annually, many brides reserve their wedding date up to four months in advance. The full deposit is applied to the cost of your final design selection.</p>
    </div>
    <div class="step">
      <div class="step__num">Step 2</div>
      <h4 class="heading">Secure The Flowers</h4>
      <p class="step__body">You can either drop your flowers off shortly after the event, or we can pick them up the night of the reception. Is your event out of town? No problem. You can ship them to us overnight or drop them off upon your return.</p>
    </div>
    <div class="step">
      <div class="step__num">Step 3</div>
      <h4 class="heading">Design Selection</h4>
      <p class="step__body">Within 30 days after your event we ask that you make an appointment to visit our showroom to make your final design selection. Once your order has been placed, it takes approximately 2 to 3 months to complete.</p>
    </div>
    <p class="process__note">Please visit our website for full details, pricing and additional pictures.<br>www.larkmeadow.com</p>
  </div>
</section>

</body>
</html>
```